NimbusFern cyber security firm Website

We did our website ourselves on Joomla, it's not great. We want a wordpress based redesign. Some thing that will represent a modern cyber security firm that's aimed at solving business problems.
Https://nimbusfern.co.nz (current site)
#58427c - primary color (you'll know why when you see it's name)
Logo files can be provided. Ask for more info if you need.

We want a modern, quick to load website. Website is going to have a home - services - products - about us - blogs menu. Will need a footer menu, site map, contact page etc.
We getting Content done sperately.
Our logo is #58427c - so hoping for a light theme (or at least the top is).
While we have been specific around the color - we are not after a website that has too much of it.

Reference sites that we like :
https://www.voltaline.co.nz/ - Love the full screen real world image
https://wardvex.co.nz/ (love the real world imagry and motion)
https://www.qtr.com/us-en?lnk=m
https://redowlen.com

Please dont use :
cartoon or redered images : (Like this : https://img.stockmorra.com/free-vector/cyber-security-concept_23-2148543851.jpg?w=2000 )

Please don't use images like this : https://www.tavelundi.com/eu/blog/oil-gas/app/uploads/2020/04/116137226_s-1440x564_c.jpg - they are old and boring.

We would like to see some creativity - loading our logo into a readymade wordpress template and hitting go won't cut it.
Updates

Thanks everyone who has submitted so far. We've extended the deadline as we wanted to give everyone a chance to Re- read the brief and perhaps make some tweeks should they feel it necessary.

Target Market(s)

Mid - large enterprise, finance, insurance, utilities vertical

Industry/Entity Type

Cyber security

Coding

Coded - Design and coding required

Number of Pages Required

5+ page

Font styles to use
Other font styles liked:
• Open sans

Colors

Designer to choose colors to be used in the design.

Requirements
Must have
• Simple clear messaging, something that catches user engagement
Nice to have
• Motion of some sort, but not overdone, GDPR

```html
<!DOCTYPE html>
<html lang="en">
<head>
<meta charset="utf-8">
<title>NimbusFern — Cyber Security</title>
<link href="https://fonts.googleapis.com/css2?family=Outfit:wght@300;400;500;600;700;800&display=swap" rel="stylesheet">
<style>
:root{
  --primary:#58427c;
  --primary-dark:#3d2a61;
  --primary-deep:#2f1f4f;
  --primary-soft:#7a63a6;
  --lavender:#cfc3e6;
  --ink:#1e1a26;
  --muted:#5b5566;
  --line:#b9b0c9;
  --white:#ffffff;
}
*{box-sizing:border-box;margin:0;padding:0}
html,body{width:1200px;height:3889px;overflow:hidden}
body{position:relative;font-family:"Outfit",sans-serif;color:var(--ink);background:var(--white)}
a{color:inherit;text-decoration:none}

/* header */
.site-header{position:absolute;left:0;top:0;width:1200px;height:95px;background:var(--white)}
.brand{position:absolute;left:98px;top:28px;display:flex;align-items:center;gap:12px}
.brand-dot{width:34px;height:34px;border-radius:50%;background:var(--primary)}
.brand-name{font-size:32px;font-weight:600;letter-spacing:1px;color:var(--primary)}
.header-bar{position:absolute;left:430px;top:0;width:770px;height:95px;background:var(--primary);clip-path:polygon(30px 0,100% 0,100% 100%,0 100%)}
.topline{position:absolute;left:0;right:0;top:12px;height:22px;display:flex;justify-content:flex-end;align-items:center;gap:16px;padding-right:100px;color:var(--white);font-size:15px}
.social{display:flex;gap:8px}
.social span{width:22px;height:22px;border-radius:50%;background:var(--white);display:block}
.topline-rule{position:absolute;left:40px;right:0;top:45px;border-top:1px solid rgba(255,255,255,.25)}
.main-nav{position:absolute;right:100px;top:58px;display:flex;gap:44px;color:var(--white);font-size:16px;font-weight:500}

/* hero */
.hero{position:absolute;left:0;top:95px;width:1200px;height:619px;background:linear-gradient(100deg,#17304f 0%,#1f5280 38%,#3a5a70 58%,#6a5a3e 80%,#2a2a30 100%)}
.hero-title{position:absolute;left:98px;top:124px;width:520px;font-size:54px;line-height:58px;font-weight:700;color:var(--white)}
.hero-sub{position:absolute;left:98px;top:318px;width:345px;font-size:17px;line-height:25px;color:var(--white)}
.btn{display:inline-flex;align-items:center;gap:14px;background:var(--primary-soft);color:var(--white);border-radius:24px;font-size:13px;font-weight:500;letter-spacing:.3px}
.btn .ico{width:16px;height:16px}
.hero .btn{position:absolute;left:98px;top:421px;height:45px;padding:0 20px}
.hero-tab{position:absolute;left:98px;top:574px;width:136px;height:45px;background:var(--white);clip-path:polygon(0 0,90% 0,100% 100%,0 100%);display:flex;gap:14px;align-items:center;padding-left:20px}
.hero-tab span{width:11px;height:11px;border-radius:50%;border:2px solid var(--primary)}
.hero-tab span.on{background:var(--primary)}

/* about */
.about-shield{position:absolute;left:98px;top:792px;width:483px;height:480px}
.eyebrow-line{display:flex;align-items:center;gap:12px;font-size:18px;color:var(--ink)}
.about-label{position:absolute;left:625px;top:804px;width:477px}
.about-label::after{content:"";flex:1;border-top:1px solid var(--line)}
.about-title{position:absolute;left:625px;top:838px;width:470px;font-size:36px;line-height:43px;font-weight:600;color:var(--primary)}
.about-copy{position:absolute;left:625px;width:477px;font-size:11.6px;line-height:18.6px;text-align:justify;color:var(--ink)}
.about .btn{position:absolute;left:625px;top:1230px;height:45px;padding:0 20px}

/* section heads */
.sec-head{position:absolute;left:0;width:1200px;text-align:center}
.sec-kicker{display:flex;justify-content:center;align-items:center;gap:14px;font-size:18px}
.sec-kicker::before,.sec-kicker::after{content:"";width:72px;border-top:1px solid currentColor}
.sec-title{margin-top:10px;font-size:44px;font-weight:700;letter-spacing:.5px}

/* services */
.services{position:absolute;left:0;top:1348px;width:1200px;height:474px;background:linear-gradient(135deg,var(--primary-dark),var(--primary) 55%,var(--primary-dark));color:var(--white)}
.svc{position:absolute;top:163px;width:320px;text-align:center}
.svc-ico{display:block;margin:0 auto;width:106px;height:106px}
.svc h3{margin-top:16px;font-size:18px;font-weight:500}
.svc p{margin:10px auto 0;width:265px;font-size:11.5px;line-height:17.5px;text-align:justify;text-align-last:center}
.svc-card{position:absolute;left:439px;top:213px;width:320px;height:200px;border:1px solid rgba(255,255,255,.6);border-radius:6px;background:rgba(255,255,255,.08)}
.svc-card-go{position:absolute;left:588px;top:402px;width:22px;height:22px;border-radius:50%;background:var(--white)}
.svc-arrow{position:absolute;top:286px;width:34px;height:34px}

/* products */
.prod{position:absolute;top:1989px;width:200px;text-align:center}
.prod svg{width:198px;height:184px;display:block;margin:0 auto}
.prod-num{position:absolute;left:83px;top:173px;width:34px;height:34px;border-radius:50%;background:var(--ink);color:var(--white);font-weight:600;font-size:16px;line-height:30px;border:2px solid var(--white)}
.prod h3{margin-top:42px;font-size:19px;line-height:24px;font-weight:400}
.link-arc{position:absolute;top:2085px;width:80px;height:30px}

/* articles */
.art-media{position:absolute;border-radius:4px}
.art-date{position:absolute;bottom:14px;left:14px;background:var(--primary);color:var(--white);font-size:14px;padding:4px 10px}
.art-cat{position:absolute;font-size:10px;letter-spacing:2px;color:var(--muted)}
.art-title{position:absolute;font-size:23px;line-height:29px;font-weight:500}
.art-text{position:absolute;font-size:11px;line-height:16px;color:var(--muted)}
.btn-sm{position:absolute;height:33px;padding:0 12px;font-size:10px;gap:10px}
.btn-sm .ico{width:13px;height:13px}

/* contact */
.contact{position:absolute;left:0;top:3029px;width:1200px;height:517px;background:linear-gradient(120deg,var(--primary-deep),var(--primary-dark) 60%,var(--primary-deep));color:var(--white)}
.contact-kicker{position:absolute;left:98px;top:56px;display:flex;align-items:center;gap:12px;font-size:18px}
.contact-kicker::after{content:"";width:72px;border-top:1px solid currentColor}
.contact-title{position:absolute;left:98px;top:92px;font-size:46px;font-weight:700}
.field{position:absolute;background:var(--white);border:1px solid var(--lavender);color:#8e879a;font-size:12px;padding:12px 12px;letter-spacing:.5px}
.send{position:absolute;left:100px;top:412px;width:560px;height:41px;background:var(--primary-soft);color:var(--white);font-size:13px;font-weight:600;text-align:center;line-height:41px}
.contact-shield{position:absolute;left:687px;top:65px;width:415px;height:414px}

/* footer */
.foot-h{position:absolute;font-size:17px;font-weight:700;color:var(--primary);letter-spacing:.3px}
.foot-links{position:absolute;left:98px;top:3638px;list-style:none;font-size:15px;line-height:25.5px}
.foot-rule{position:absolute;top:3600px;height:175px;border-left:1px solid var(--line)}
.foot-item{position:absolute;left:311px;display:flex;gap:14px;font-size:14px;line-height:20px}
.foot-item svg{width:16px;height:16px;flex:none;margin-top:2px}
.foot-map{position:absolute;left:563px;top:3592px;width:223px;height:181px;border:2px solid var(--primary);border-radius:6px;background:linear-gradient(160deg,#f1f0f3,#e4e6e2)}
.foot-brand{position:absolute;left:838px;top:3600px;width:264px;text-align:center}
.foot-brand .dot{width:58px;height:58px;border-radius:50%;background:var(--primary);margin:0 auto}
.foot-brand .name{margin-top:14px;font-size:34px;font-weight:600;color:var(--primary);letter-spacing:1px}
.foot-follow{margin-top:24px;display:flex;justify-content:center;align-items:center;gap:10px;font-size:17px;color:var(--primary)}
.foot-follow .social span{background:var(--primary)}
.copyright{position:absolute;left:0;top:3822px;width:1200px;height:67px;background:var(--primary);color:var(--white);font-size:13px;text-align:center;line-height:60px}
</style>
</head>
<body>

<header class="site-header">
  <div class="brand"><span class="brand-dot"></span><span class="brand-name">NIMBUSFERN</span></div>
  <div class="header-bar">
    <div class="topline">
      <span>&#9742;&nbsp; +64 (0) 210 555 0142</span><span>|</span>
      <span>&#9993;&nbsp; info@nimbusfern.co.nz</span>
      <span>Follow Us</span>
      <div class="social"><span></span><span></span><span></span></div>
    </div>
    <div class="topline-rule"></div>
    <nav class="main-nav"><a>Home</a><a>Services</a><a>Products</a><a>About us</a><a>Blogs</a><a>Contact Us</a></nav>
  </div>
</header>

<section class="hero" role="img" aria-label="Aerial photo of a coastal city skyline at dusk with a long beach and lit streets">
  <h1 class="hero-title">Save time and resources in cyber risk assessments</h1>
  <p class="hero-sub">Calculate, reduce and monitor human cyber risk with the new-class of user-focused security.</p>
  <a class="btn">LEARN MORE
    <svg class="ico" viewBox="0 0 16 16" fill="none" stroke="#fff" stroke-width="1.6"><path d="M2 8h11M9 4l4 4-4 4"/></svg></a>
  <div class="hero-tab"><span class="on"></span><span></span><span></span><span></span></div>
</section>

<section class="about">
  <svg class="about-shield" viewBox="0 0 483 480" role="img" aria-label="Photo of a woman using a tablet in a server room, framed in a shield">
    <defs><linearGradient id="aboutFill" x1="0" y1="0" x2="1" y2="1"><stop offset="0" stop-color="#1d3f78"/><stop offset=".55" stop-color="#3b5f95"/><stop offset="1" stop-color="#1b2a4c"/></linearGradient></defs>
    <path d="M242 0 C170 0 70 20 0 60 L8 250 C25 360 130 440 242 480 C354 440 458 360 475 250 L483 60 C413 20 314 0 242 0Z" fill="var(--primary)"/>
    <path d="M242 14 C175 14 85 32 16 70 L24 250 C40 350 138 422 242 460 C346 422 444 350 460 250 L467 70 C398 32 309 14 242 14Z" fill="url(#aboutFill)"/>
  </svg>
  <div class="about-label eyebrow-line">About Us</div>
  <h2 class="about-title">The tech you use to run your business could be used to sabotage it!</h2>
  <p class="about-copy" style="top:982px">In the course of doing business, your company could deal with dozens of third-party vendors: suppliers, manufacturers, service providers, affiliate offices, distributors, resellers, agents, contractors, the list goes on … all of whom, in turn, deal with dozens of their own vendors. It's easy to see then why third-party cyber risk management is becoming such a high priority for businesses that deal with confidential data. (Lawyers, accountants, insurers, to name just three.)</p>
  <p class="about-copy" style="top:1112px">NimbusFern is a 100% New Zealand owned and operated cyber security company, designed to protect your business against exactly this kind of risk by offering third-party risk management and cyber security solutions. In short, offering small and medium sized businesses the same standard of cyber security as a large organisations – at a price that makes sense.</p>
  <a class="btn">LEARN MORE
    <svg class="ico" viewBox="0 0 16 16" fill="none" stroke="#fff" stroke-width="1.6"><path d="M2 8h11M9 4l4 4-4 4"/></svg></a>
</section>

<section class="services">
  <div class="sec-head" style="top:36px"><div class="sec-kicker">NimbusFern</div><h2 class="sec-title">OUR SERVICES</h2></div>

  <div class="svc-card"></div>
  <div class="svc-card-go"><svg viewBox="0 0 22 22" width="22" height="22"><path d="M6 11h10M12 7l4 4-4 4" stroke="var(--primary)" stroke-width="2" fill="none"/></svg></div>

  <div class="svc" style="left:98px">
    <svg class="svc-ico" viewBox="0 0 106 106"><path d="M53 2 C35 10 18 12 4 12 L4 54 C4 78 28 96 53 104 C78 96 102 78 102 54 L102 12 C88 12 71 10 53 2Z" fill="#fff" stroke="var(--primary-dark)" stroke-width="3"/><circle cx="53" cy="48" r="20" fill="none" stroke="var(--primary)" stroke-width="2.5"/></svg>
    <h3>Virtual CISO</h3>
    <p>Lorem Ipsum is simply dummy text of the printing and typesetting industry. Lorem Ipsum has been the industry's standard dummy text ever since the 1500s, when an unknown.</p>
  </div>
  <div class="svc" style="left:439px;top:164px">
    <svg class="svc-ico" viewBox="0 0 106 106" style="width:118px;height:118px"><path d="M53 2 C35 10 18 12 4 12 L4 54 C4 78 28 96 53 104 C78 96 102 78 102 54 L102 12 C88 12 71 10 53 2Z" fill="#fff" stroke="var(--primary-dark)" stroke-width="3"/><rect x="32" y="32" width="42" height="30" rx="3" fill="none" stroke="var(--primary)" stroke-width="2.5"/></svg>
    <h3 style="margin-top:8px">Cyber Security assessments</h3>
    <p>Lorem Ipsum is simply dummy text of the printing and typesetting industry. Lorem Ipsum has been the industry's standard dummy text ever since the 1500s, when an unknown.</p>
  </div>
  <div class="svc" style="left:780px">
    <svg class="svc-ico" viewBox="0 0 106 106"><path d="M53 2 C35 10 18 12 4 12 L4 54 C4 78 28 96 53 104 C78 96 102 78 102 54 L102 12 C88 12 71 10 53 2Z" fill="#fff" stroke="var(--primary-dark)" stroke-width="3"/><rect x="38" y="28" width="30" height="40" rx="3" fill="none" stroke="var(--primary)" stroke-width="2.5"/><path d="M44 40h18M44 48h18M44 56h12" stroke="var(--primary)" stroke-width="2"/></svg>
    <h3>Third-party Risk Management</h3>
    <p>Lorem Ipsum is simply dummy text of the printing and typesetting industry. Lorem Ipsum has been the industry's standard dummy text ever since the 1500s, when an unknown.</p>
  </div>

  <svg class="svc-arrow" style="left:51px" viewBox="0 0 34 34"><circle cx="17" cy="17" r="15.5" fill="none" stroke="#fff" stroke-width="1.5"/><path d="M19 11l-6 6 6 6" fill="none" stroke="#fff" stroke-width="1.8"/></svg>
  <svg class="svc-arrow" style="left:1116px" viewBox="0 0 34 34"><circle cx="17" cy="17" r="15.5" fill="none" stroke="#fff" stroke-width="1.5"/><path d="M15 11l6 6-6 6" fill="none" stroke="#fff" stroke-width="1.8"/></svg>
</section>

<section class="products">
  <div class="sec-head" style="top:1873px;color:var(--primary)"><div class="sec-kicker">NimbusFern</div><h2 class="sec-title">OUR PRODUCTS</h2></div>

  <div class="prod" style="left:98px">
    <svg viewBox="0 0 198 184"><path d="M99 0 C60 2 25 10 0 22 L4 90 C12 140 55 170 99 184 C143 170 186 140 194 90 L198 22 C173 10 138 2 99 0Z" fill="var(--primary)"/><path d="M99 22 C66 24 38 30 18 40 L22 92 C30 130 64 154 99 166 C134 154 168 130 176 92 L180 40 C160 30 132 24 99 22Z" fill="var(--primary-soft)" opacity=".55"/><circle cx="99" cy="92" r="30" fill="none" stroke="#fff" stroke-width="6"/></svg>
    <div class="prod-num">1</div>
    <h3>Third Party<br>Risk Management</h3>
  </div>
  <div class="prod" style="left:366px">
    <svg viewBox="0 0 198 184"><path d="M99 0 C60 2 25 10 0 22 L4 90 C12 140 55 170 99 184 C143 170 186 140 194 90 L198 22 C173 10 138 2 99 0Z" fill="var(--primary)"/><path d="M99 22 C66 24 38 30 18 40 L22 92 C30 130 64 154 99 166 C134 154 168 130 176 92 L180 40 C160 30 132 24 99 22Z" fill="var(--primary-soft)" opacity=".55"/><path d="M99 58 L124 68 L124 92 C124 108 112 118 99 124 C86 118 74 108 74 92 L74 68Z" fill="none" stroke="#fff" stroke-width="6"/></svg>
    <div class="prod-num">2</div>
    <h3>Brindle Cloud<br>Based Security</h3>
  </div>
  <div class="prod" style="left:635px">
    <svg viewBox="0 0 198 184"><path d="M99 0 C60 2 25 10 0 22 L4 90 C12 140 55 170 99 184 C143 170 186 140 194 90 L198 22 C173 10 138 2 99 0Z" fill="var(--primary)"/><path d="M99 22 C66 24 38 30 18 40 L22 92 C30 130 64 154 99 166 C134 154 168 130 176 92 L180 40 C160 30 132 24 99 22Z" fill="var(--primary-soft)" opacity=".55"/><rect x="62" y="56" width="64" height="58" rx="4" fill="none" stroke="#fff" stroke-width="6"/><circle cx="118" cy="108" r="18" fill="var(--primary)" stroke="#fff" stroke-width="6"/></svg>
    <div class="prod-num">3</div>
    <h3>Vulnerability<br>Management</h3>
  </div>
  <div class="prod" style="left:903px">
    <svg viewBox="0 0 198 184"><path d="M99 0 C60 2 25 10 0 22 L4 90 C12 140 55 170 99 184 C143 170 186 140 194 90 L198 22 C173 10 138 2 99 0Z" fill="var(--primary)"/><path d="M99 22 C66 24 38 30 18 40 L22 92 C30 130 64 154 99 166 C134 154 168 130 176 92 L180 40 C160 30 132 24 99 22Z" fill="var(--primary-soft)" opacity=".55"/><path d="M84 80 V66 a15 15 0 0 1 30 0 V80" fill="none" stroke="#fff" stroke-width="7"/><rect x="74" y="80" width="50" height="40" rx="4" fill="#fff"/></svg>
    <div class="prod-num">4</div>
    <h3>KeyHarbor Password<br>Management</h3>
  </div>

  <svg class="link-arc" style="left:290px" viewBox="0 0 80 30"><path d="M4 22 Q40 -4 74 22" fill="none" stroke="#9b93a8" stroke-width="2" stroke-dasharray="3 4"/><path d="M68 16l7 7-9 1" fill="none" stroke="#9b93a8" stroke-width="2"/></svg>
  <svg class="link-arc" style="left:558px" viewBox="0 0 80 30"><path d="M4 22 Q40 -4 74 22" fill="none" stroke="#9b93a8" stroke-width="2" stroke-dasharray="3 4"/><path d="M68 16l7 7-9 1" fill="none" stroke="#9b93a8" stroke-width="2"/></svg>
  <svg class="link-arc" style="left:826px" viewBox="0 0 80 30"><path d="M4 22 Q40 -4 74 22" fill="none" stroke="#9b93a8" stroke-width="2" stroke-dasharray="3 4"/><path d="M68 16l7 7-9 1" fill="none" stroke="#9b93a8" stroke-width="2"/></svg>
</section>

<section class="articles">
  <div class="sec-head" style="top:2356px;color:var(--primary)"><div class="sec-kicker">NimbusFern</div><h2 class="sec-title">RECENT ARTICLES</h2></div>

  <div class="art-media" style="left:98px;top:2481px;width:491px;height:293px;background:linear-gradient(120deg,#0f2f4a,#2c5f86 50%,#14263c)" role="img" aria-label="Photo of a developer working at several monitors in a dark office"><span class="art-date">May 12, 2017</span></div>
  <div class="art-cat" style="left:108px;top:2802px">CYBER SECURITY</div>
  <h3 class="art-title" style="left:108px;top:2826px">Lorem Ipsum is simply dummy text</h3>
  <p class="art-text" style="left:108px;top:2864px;width:480px">Lorem ipsum dolor sit amet, consectetur adipisicing elit, sed do eiusmod tempor incididunt ut labore et dolore magna aliqua. Ut enim.</p>
  <a class="btn btn-sm" style="left:106px;top:2913px">LEARN MORE
    <svg class="ico" viewBox="0 0 16 16" fill="none" stroke="#fff" stroke-width="1.6"><path d="M2 8h11M9 4l4 4-4 4"/></svg></a>

  <div class="art-media" style="left:611px;top:2481px;width:233px;height:216px;background:linear-gradient(140deg,#e9ecef,#b7bcc4 60%,#8a8f99)" role="img" aria-label="Photo of hands typing on a laptop with a security lock overlay"><span class="art-date">May 12, 2017</span></div>
  <div class="art-cat" style="left:881px;top:2481px">CYBER SECURITY</div>
  <h3 class="art-title" style="left:881px;top:2508px;width:220px">Lorem Ipsum is simply dummy text</h3>
  <p class="art-text" style="left:881px;top:2580px;width:222px">Lorem ipsum dolor sit amet, consectetur adipisicing elit, sed do eiusmod tempor incididunt ut labore et dolore magna aliqua. Ut enim.</p>
  <a class="btn btn-sm" style="left:880px;top:2665px">LEARN MORE
    <svg class="ico" viewBox="0 0 16 16" fill="none" stroke="#fff" stroke-width="1.6"><path d="M2 8h11M9 4l4 4-4 4"/></svg></a>

  <div class="art-media" style="left:611px;top:2730px;width:233px;height:216px;background:linear-gradient(140deg,#c9dcee,#6f96c4 55%,#3d5f95)" role="img" aria-label="Photo of a laptop keyboard with glowing padlock icons"><span class="art-date">May 12, 2017</span></div>
  <div class="art-cat" style="left:881px;top:2730px">CYBER SECURITY</div>
  <h3 class="art-title" style="left:881px;top:2757px;width:220px">Lorem Ipsum is simply dummy text</h3>
  <p class="art-text" style="left:881px;top:2829px;width:222px">Lorem ipsum dolor sit amet, consectetur adipisicing elit, sed do eiusmod tempor incididunt ut labore et dolore magna aliqua. Ut enim.</p>
  <a class="btn btn-sm" style="left:880px;top:2913px">LEARN MORE
    <svg class="ico" viewBox="0 0 16 16" fill="none" stroke="#fff" stroke-width="1.6"><path d="M2 8h11M9 4l4 4-4 4"/></svg></a>
</section>

<section class="contact">
  <div class="contact-kicker">NimbusFern</div>
  <h2 class="contact-title">CONTACT FORM</h2>
  <div class="field" style="left:100px;top:170px;width:276px;height:41px">FIRST NAME*</div>
  <div class="field" style="left:383px;top:170px;width:277px;height:41px">LAST NAME*</div>
  <div class="field" style="left:100px;top:222px;width:276px;height:41px">E-MAIL*</div>
  <div class="field" style="left:383px;top:222px;width:277px;height:41px">PHONE*</div>
  <div class="field" style="left:100px;top:273px;width:560px;height:126px">MESSAGE</div>
  <div class="send">SEND NOW</div>
  <svg class="contact-shield" viewBox="0 0 415 414" role="img" aria-label="Photo of hands on a keyboard with digital security graphics, framed in a shield">
    <defs><linearGradient id="contactFill" x1="0" y1="0" x2="1" y2="1"><stop offset="0" stop-color="#c9a48a"/><stop offset=".5" stop-color="#8a6f78"/><stop offset="1" stop-color="#4a3b5e"/></linearGradient></defs>
    <path d="M207 0 C140 0 60 18 0 50 L6 220 C22 310 110 380 207 414 C304 380 393 310 409 220 L415 50 C355 18 274 0 207 0Z" fill="var(--primary)"/>
    <path d="M207 14 C145 14 72 30 16 60 L22 220 C36 300 118 364 207 396 C296 364 379 300 393 220 L399 60 C343 30 269 14 207 14Z" fill="url(#contactFill)"/>
  </svg>
</section>

<footer>
  <div class="foot-h" style="left:98px;top:3594px">QUICK LINKS</div>
  <ul class="foot-links"><li>Home</li><li>Services</li><li>Products</li><li>About us</li><li>Blogs</li><li>Contact Us</li></ul>
  <div class="foot-rule" style="left:253px"></div>

  <div class="foot-h" style="left:311px;top:3594px">CONTACT US</div>
  <div class="foot-item" style="top:3638px">
    <svg viewBox="0 0 16 16"><path d="M8 1a5 5 0 0 1 5 5c0 4-5 9-5 9S3 10 3 6a5 5 0 0 1 5-5z" fill="var(--primary)"/><circle cx="8" cy="6" r="2" fill="#fff"/></svg>
    <span>42b Harlow Street, Kelvale,<br>Rivermouth, 4810</span></div>
  <div class="foot-item" style="top:3703px">
    <svg viewBox="0 0 16 16"><circle cx="8" cy="8" r="8" fill="var(--primary)"/><path d="M5 4l2 2-1 1c.6 1.3 1.7 2.4 3 3l1-1 2 2-1 1.5C7.5 12 4 8.5 3.5 5z" fill="#fff"/></svg>
    <span>+64 (0) 210 555 0142</span></div>
  <div class="foot-item" style="top:3757px">
    <svg viewBox="0 0 16 16"><circle cx="8" cy="8" r="8" fill="var(--primary)"/><rect x="4" y="5" width="8" height="6" fill="none" stroke="#fff" stroke-width="1.2"/><path d="M4 5l4 3 4-3" fill="none" stroke="#fff" stroke-width="1.2"/></svg>
    <span>info@nimbusfern.co.nz</span></div>
  <div class="foot-rule" style="left:531px"></div>

  <div class="foot-map" role="img" aria-label="Street map showing the office location"></div>
  <div class="foot-rule" style="left:816px"></div>

  <div class="foot-brand">
    <div class="dot"></div>
    <div class="name">NIMBUSFERN</div>
    <div class="foot-follow">Follow Us <div class="social"><span></span><span></span><span></span></div></div>
  </div>

  <div class="copyright">© Copyright - 2022 &nbsp;|&nbsp; NimbusFern &nbsp;|&nbsp; All Rights Reserved</div>
</footer>

</body>
</html>
```